FinchMoor Pet - Cat Snack Range Packaging Design

Cat Velvo is a tasty snack for pets that comes in 3 flavors: Salmon, Tuna, Chicken. Each pack has 5 sticks.

Designs are currently too "cartoon-ish"; looking to refresh design into a high-end, "professional" product.

Prefer to have black/dark background with different colors for each flavor, but also open to designers' own creative take, as long as product looks professional.

Can refer to cat food brand "Gilden Paws" and "Trib" photo attached for reference.
https://www.gildenpaws-example.com/us/cats/products/vet-products

Looking to expand the design concept in the future to a whole range of cat products, such as cat litter, dental chewing sticks, canned cat food, etc.

Target Market(s)

More premium, high-end pet owners

Colors

Designer to choose only greyscale colors for use in the design.

Requirements
Must have
• Professional look
Nice to have
• Design template that can be copied and used for various product ranges (cat snacks, cans, litter, etc)

```html
<!DOCTYPE html>
<html lang="en">
<head>
<meta charset="UTF-8">
<title>FinchMoor Pet – Cat Velvo Mini Pouch Range</title>
<link href="https://fonts.googleapis.com/css2?family=Lexend:wght@600;700&family=Kalam:wght@700&family=Poppins:wght@600&display=swap" rel="stylesheet">
<style>
  :root {
    --backdrop: #f4eee9;
    --pouch: #232425;
    --window: #d4d5d6;
    --text-light: #ffffff;
    --tuna: #1c9e8c;
    --salmon: #3aa9e4;
    --chicken: #df8c80;
    --photo-dark: #4a4a4a;
    --photo-light: #9a9a9a;
    --mascot-light: #eeeae6;
    --mascot-dark: #9d9a97;
  }
  * { margin: 0; padding: 0; box-sizing: border-box; }
  html, body { width: 1200px; height: 900px; overflow: hidden; }
  body { background: var(--backdrop); position: relative; }

  .range { position: absolute; inset: 0; }

  .pouch {
    position: absolute;
    width: 345px; height: 535px;
    background: var(--pouch);
    border-radius: 16px 16px 18px 18px;
    overflow: hidden;
    color: var(--text-light);
    text-align: center;
    transform-origin: top left;
  }
  .pouch--tuna    { left: 59px;  top: 170px; --accent: var(--tuna); }
  .pouch--salmon  { left: 422px; top: 152px; --accent: var(--salmon); transform: scale(1.09); z-index: 2; }
  .pouch--chicken { left: 820px; top: 170px; --accent: var(--chicken); }

  .hang-slot {
    position: absolute; top: 32px; left: 50%;
    width: 72px; height: 12px; margin-left: -36px;
    border-radius: 6px; background: var(--backdrop);
  }
  .mascot {
    position: absolute; top: 56px; left: 50%;
    width: 84px; height: 82px; margin-left: -42px;
    border-radius: 40% 40% 34% 34%;
    background: radial-gradient(circle at 50% 40%, var(--mascot-light) 55%, var(--mascot-dark));
  }
  .brand {
    position: absolute; top: 140px; left: 0; right: 0;
    font: 700 20px/1 "Lexend", sans-serif;
    letter-spacing: 0.5px;
  }
  .product-name {
    position: absolute; top: 164px; left: 0; right: 0;
    font: 700 40px/1 "Lexend", sans-serif;
    letter-spacing: 1.5px;
  }
  .tagline {
    position: absolute; top: 207px; left: 0; right: 0;
    font: 700 12px/1 "Kalam", cursive;
    letter-spacing: 0.8px;
  }
  .flavour {
    position: absolute; top: 234px; left: 0; right: 0;
    font: 700 21px/1 "Lexend", sans-serif;
    color: var(--accent);
    letter-spacing: 1px;
  }
  .extra {
    position: absolute; top: 261px; left: 0; right: 0;
    font: 700 11.5px/1 "Kalam", cursive;
    letter-spacing: 0.6px;
  }
  .window {
    position: absolute; top: 292px; left: 47px;
    width: 234px; height: 176px;
    border-radius: 10px;
    background: linear-gradient(180deg, #e0e1e2, var(--window));
  }
  .colour-band { position: absolute; inset: 0; }
  .cat-photo {
    position: absolute; right: 0; bottom: 0;
    width: 190px; height: 238px;
    border-radius: 90px 60px 0 0;
    background: linear-gradient(160deg, var(--photo-light), var(--photo-dark) 70%);
  }
  .natural-badge {
    position: absolute; left: 20px; top: 468px;
    width: 52px; text-align: center;
  }
  .natural-badge svg { display: block; margin: 0 auto; }
  .natural-badge span {
    display: block; margin-top: 3px;
    font: 600 9px/1 "Poppins", sans-serif;
    color: var(--text-light);
  }
  .protein-icon {
    position: absolute; left: 84px; top: 470px;
    width: 46px; height: 40px;
    border-radius: 50% 40% 45% 45%;
    background: rgba(35, 36, 37, 0.35);
  }
  .net-weight {
    position: absolute; left: 12px; bottom: 8px;
    font: 600 10.5px/1 "Poppins", sans-serif;
    color: var(--text-light);
  }
</style>
</head>
<body>
<main class="range">

  <section class="pouch pouch--tuna">
    <div class="hang-slot"></div>
    <div class="mascot" role="img" aria-label="Brand mascot illustration of a spotted cub"></div>
    <div class="brand">FinchMoor Pet</div>
    <h1 class="product-name">CAT VELVO</h1>
    <p class="tagline">HEALTHY, TASTY &amp; NATURAL!</p>
    <h2 class="flavour">TUNA MINI POUCH</h2>
    <p class="extra">WITH EXTRA - ADDED CRANBERRY</p>
    <div class="window"></div>
    <svg class="colour-band" viewBox="0 0 345 535" preserveAspectRatio="none" aria-hidden="true">
      <path d="M0 440 C110 425 240 370 345 300 L345 535 L0 535 Z" fill="var(--tuna)"/>
    </svg>
    <div class="cat-photo" role="img" aria-label="Photo of a seated long-haired tabby cat"></div>
    <div class="natural-badge">
      <svg width="30" height="30" viewBox="0 0 30 30" aria-hidden="true"><circle cx="15" cy="15" r="13" fill="none" stroke="#fff" stroke-width="2"/><path d="M10 20 C10 12 15 9 21 9 C21 16 17 20 10 20 Z M10 20 L17 13" fill="none" stroke="#fff" stroke-width="1.8"/></svg>
      <span>NATURAL</span>
    </div>
    <div class="protein-icon" role="img" aria-label="Chicken outline icon"></div>
    <p class="net-weight">NET: 75 G ( 15GX5)</p>
  </section>

  <section class="pouch pouch--salmon">
    <div class="hang-slot"></div>
    <div class="mascot" role="img" aria-label="Brand mascot illustration of a spotted cub"></div>
    <div class="brand">FinchMoor Pet</div>
    <h1 class="product-name">CAT VELVO</h1>
    <p class="tagline">HEALTHY, TASTY &amp; NATURAL!</p>
    <h2 class="flavour">SALMON MINI POUCH</h2>
    <p class="extra">WITH EXTRA - ADDED OMEGA 3</p>
    <div class="window"></div>
    <svg class="colour-band" viewBox="0 0 345 535" preserveAspectRatio="none" aria-hidden="true">
      <path d="M0 440 C110 425 240 370 345 300 L345 535 L0 535 Z" fill="var(--salmon)"/>
    </svg>
    <div class="cat-photo" role="img" aria-label="Photo of a seated long-haired tabby cat"></div>
    <div class="natural-badge">
      <svg width="30" height="30" viewBox="0 0 30 30" aria-hidden="true"><circle cx="15" cy="15" r="13" fill="none" stroke="#fff" stroke-width="2"/><path d="M10 20 C10 12 15 9 21 9 C21 16 17 20 10 20 Z M10 20 L17 13" fill="none" stroke="#fff" stroke-width="1.8"/></svg>
      <span>NATURAL</span>
    </div>
    <div class="protein-icon" role="img" aria-label="Chicken outline icon"></div>
    <p class="net-weight">NET: 75 G ( 15GX5)</p>
  </section>

  <section class="pouch pouch--chicken">
    <div class="hang-slot"></div>
    <div class="mascot" role="img" aria-label="Brand mascot illustration of a spotted cub"></div>
    <div class="brand">FinchMoor Pet</div>
    <h1 class="product-name">CAT VELVO</h1>
    <p class="tagline">HEALTHY, TASTY &amp; NATURAL!</p>
    <h2 class="flavour">CHICKEN MINI POUCH</h2>
    <p class="extra">WITH EXTRA - ADDED CAT GRASS</p>
    <div class="window"></div>
    <svg class="colour-band" viewBox="0 0 345 535" preserveAspectRatio="none" aria-hidden="true">
      <path d="M0 440 C110 425 240 370 345 300 L345 535 L0 535 Z" fill="var(--chicken)"/>
    </svg>
    <div class="cat-photo" role="img" aria-label="Photo of a seated long-haired tabby cat"></div>
    <div class="natural-badge">
      <svg width="30" height="30" viewBox="0 0 30 30" aria-hidden="true"><circle cx="15" cy="15" r="13" fill="none" stroke="#fff" stroke-width="2"/><path d="M10 20 C10 12 15 9 21 9 C21 16 17 20 10 20 Z M10 20 L17 13" fill="none" stroke="#fff" stroke-width="1.8"/></svg>
      <span>NATURAL</span>
    </div>
    <div class="protein-icon" role="img" aria-label="Chicken outline icon"></div>
    <p class="net-weight">NET: 75 G ( 15GX5)</p>
  </section>

</main>
</body>
</html>
```